Copper Harbor Athletics

COPPER HARBOR ATHLETICS PTY LTD, We are a revolutionary, fresh, new entity to the fitness industry looking to make a mark within and support local communities where we are situated. My business partner and i come with a broad range of skill sets and possess the ability and motivation to ensure our philosophy works - and the philosophy is simple - to help people improve their everyday life and well-being. Be it, helping them with their health and fitness, changing their appearance, improving motivation, setting and achieving goals or by helping them become part of a positive team atmosphere.
Our stores visual appearance, like our training concepts, is quite different to the normal run of the mill gym. It's fresh, it's vibrant, it looks great, and we know it will be a real head turner guaranteed to attract attention. This is definitely the future of fitness.
We would like to see on one side our Info and on the other side our LOGO, colour scheme is in the LOGO.
Final design should tell people "We Help People Stand Tall And Shine Like Copper!

Industry/Entity Type

Training

Contact Information for Business Card

Marcus
0417 362 591
marc@copperharborathletics.com.au
217 Glenview Rd East Balcombe NSW 2100

Requirements
Must have
• Our Logo

```html
<!DOCTYPE html>
<html lang="en">
<head>
<meta charset="utf-8">
<title>Copper Harbor Athletics – Business Card</title>
<link rel="stylesheet" href="https://fonts.googleapis.com/css2?family=Michroma&family=Jura:wght@600;700&display=swap">
<style>
  :root {
    --navy: #10164a;
    --navy-glow: #232a6b;
    --band-light: #ffffff;
    --band-edge: #e3e3e5;
    --ink: #141a4e;
    --front-type: #f2f3f8;
    --backdrop: #e9e7e3;
    --mark-square: #141a4e;
  }
  * { box-sizing: border-box; margin: 0; padding: 0; }
  html, body {
    width: 1200px; height: 957px; overflow: hidden;
    background: var(--backdrop);
  }
  .stage { position: relative; width: 1200px; height: 957px; }

  .card { position: absolute; border-radius: 30px; overflow: hidden; }

  .card-front {
    left: 272px; top: 70px; width: 670px; height: 385px;
    background: radial-gradient(ellipse 55% 60% at 50% 45%, var(--navy-glow) 0%, var(--navy) 100%);
    display: flex; align-items: center; justify-content: center;
  }
  .front-title {
    font-family: "Michroma", sans-serif;
    font-size: 19px; letter-spacing: 0.5px;
    color: var(--front-type);
    margin-top: -116px;
  }

  .card-back {
    left: 264px; top: 508px; width: 678px; height: 389px;
    background: var(--navy);
  }
  .info-band {
    position: absolute; left: 0; top: 70px; width: 100%; height: 250px;
    background: radial-gradient(ellipse 45% 60% at 52% 50%, var(--band-light) 0%, var(--band-edge) 100%);
  }
  .brand-mark {
    position: absolute; left: 48px; top: 62px; width: 150px;
    display: flex; flex-direction: column; align-items: flex-start; gap: 10px;
    font-family: "Jura", sans-serif; font-weight: 700;
    font-size: 17px; line-height: 1.15; color: var(--ink);
  }
  .brand-square { width: 26px; height: 26px; background: var(--mark-square); }

  .contact {
    position: absolute; left: 364px; top: 103px;
    font-family: "Jura", sans-serif; font-weight: 700; color: var(--ink);
  }
  .contact-name { font-size: 21px; letter-spacing: 0.5px; margin-bottom: 2px; }
  .contact-line { font-size: 12.5px; margin-left: 2px; line-height: 17px; }
  .contact-line.address { font-size: 9.5px; line-height: 15px; }
  .contact-line.email { font-size: 12.5px; margin-left: 0; }
</style>
</head>
<body>
<main class="stage">
  <section class="card card-front">
    <h1 class="front-title">COPPER HARBOR ATHLETICS</h1>
  </section>

  <section class="card card-back">
    <div class="info-band">
      <div class="brand-mark">
        <span class="brand-square"></span>
        <span class="brand-name">Copper Harbor Athletics</span>
      </div>
      <div class="contact">
        <p class="contact-name">Marcus</p>
        <p class="contact-line phone">Phone :&nbsp; 0417 362 591</p>
        <p class="contact-line address">Adress : 217 Glenview Rd East Balcombe NSW 2100</p>
        <p class="contact-line email">Email : marc@copperharborathletics.com.au</p>
      </div>
    </div>
  </section>
</main>
</body>
</html>
```